Real Estate Investment Company needs postcard design

We need a postcard design for a Real Estate Investment company named 'Bright Harbor Holdings, LLC'. We are a residential redevelopment company who specializes in buying distressed homes at a significant discount, and renovate and resell them to retail home buyers and landlords. Our service is to give home owners an option to contact us if they want to sell their home. We would like to see designs that use our logo with a modern and friendly feel. These post cards will be going out to clients who are in stressful situations (foreclosure, estate sales, etc.) and would like them to feel comfortable and safe when receiving this postcard. The final design should communicate stress free and fast solution for their situation.
Real Estate

```html
<!DOCTYPE html>
<html lang="en">
<head>
<meta charset="utf-8">
<title>Bright Harbor Holdings – Postcard</title>
<link rel="stylesheet" href="https://fonts.googleapis.com/css2?family=Archivo+Black&family=Open+Sans:wght@400;600;700;800&family=Permanent+Marker&family=Anton&family=Open+Sans+Condensed:wght@300;700&display=swap">
<style>
  :root {
    --backdrop: #efe6d6;
    --yellow: #f8c400;
    --blue: #2f7fd6;
    --blue-dark: #1f63b5;
    --ink: #111111;
    --body-ink: #2a2a2a;
    --red: #e4151b;
    --white: #ffffff;
    --back-light: #eef3fb;
    --back-edge: #a9c8ef;
  }
  * { box-sizing: border-box; margin: 0; padding: 0; }
  html, body { width: 1200px; height: 508px; overflow: hidden; }
  body {
    background: var(--backdrop);
    position: relative;
    font-family: "Open Sans", Arial, sans-serif;
  }
  .card {
    position: absolute;
    top: 55px;
    width: 517px;
    height: 400px;
    overflow: hidden;
  }

  /* Front */
  .card-front { left: 55px; background: var(--yellow); }
  .front-headline {
    position: absolute; top: 12px; left: 0; width: 100%;
    text-align: center;
    font-family: "Permanent Marker", cursive;
    font-size: 27px; color: var(--ink); letter-spacing: 0.5px;
  }
  .front-title {
    position: absolute; top: 44px; left: 0; width: 100%;
    text-align: center;
    font-family: "Archivo Black", Arial, sans-serif;
    font-size: 50px; line-height: 60px; color: var(--blue);
  }
  .benefit-band {
    position: absolute; top: 104px; left: 0; width: 100%; height: 31px;
    background: var(--blue); color: var(--white);
    font-weight: 600; font-size: 20px; line-height: 31px;
    text-align: center; white-space: nowrap;
  }
  .hero-photo {
    position: absolute; top: 135px; left: 0; width: 100%; height: 222px;
    background: linear-gradient(160deg, #b9c9d6 0%, #d9dde0 35%, #c23a33 55%, #7d9a62 85%, #5f8048 100%);
  }
  .hero-swoosh { position: absolute; top: 135px; left: 0; width: 517px; height: 222px; }
  .brand-name {
    position: absolute; top: 160px; left: 322px; width: 180px;
    font-weight: 800; font-size: 19px; line-height: 22px;
    color: var(--blue-dark); text-align: center;
  }
  .call-band {
    position: absolute; bottom: 0; left: 0; width: 100%; height: 43px;
    display: flex; align-items: center; justify-content: center; gap: 12px;
    font-weight: 800; font-size: 19px;
  }
  .call-label { color: var(--ink); }
  .call-number { color: var(--blue-dark); display: flex; align-items: center; gap: 6px; font-size: 21px; }

  /* Back */
  .card-back {
    left: 628px;
    background: linear-gradient(90deg, var(--back-edge) 0%, var(--back-light) 35%, var(--back-light) 100%);
  }
  .back-heading {
    position: absolute; top: 13px; left: 0; width: 257px; height: 45px;
    background: var(--blue); color: var(--white);
    padding: 3px 0 0 17px; font-size: 14.5px; line-height: 20px;
  }
  .back-copy {
    position: absolute; top: 68px; left: 17px; width: 245px;
    font-size: 11.5px; line-height: 15.5px; color: var(--body-ink);
  }
  .back-copy p { margin-bottom: 6px; }
  .back-copy .alert { color: var(--red); font-weight: 700; font-size: 15.5px; margin: 4px 0 6px; }
  .back-promise {
    position: absolute; top: 252px; left: 0; width: 257px;
    text-align: center; color: var(--red);
    font-family: "Archivo Black", Arial, sans-serif;
    font-size: 19px; line-height: 22px;
  }
  .back-call {
    position: absolute; top: 307px; left: 0; width: 257px; height: 27px;
    background: var(--blue); color: var(--white);
    display: flex; align-items: center; justify-content: center; gap: 5px;
    font-size: 14px;
  }
  .return-brand {
    position: absolute; top: 30px; left: 280px; width: 150px;
    font-weight: 800; font-size: 14px; line-height: 17px; color: var(--blue-dark);
  }
  .return-address {
    position: absolute; top: 74px; left: 310px;
    font-size: 9.5px; line-height: 12px; color: var(--body-ink);
  }
  .stamp-box {
    position: absolute; top: 15px; left: 430px; width: 70px; height: 58px;
    border: 2px dashed #333;
  }
</style>
</head>
<body>

<section class="card card-front">
  <h2 class="front-headline">NEED TO SELL YOUR HOUSE FAST?</h2>
  <h1 class="front-title">WE BUY HOUSES</h1>
  <div class="benefit-band">Get Cash FAST &nbsp;•&nbsp; Any Condition &nbsp;•&nbsp; Close Quick</div>
  <div class="hero-photo" role="img" aria-label="Photo of a house with a foreclosure for-sale sign, one hand passing house keys and another passing a stack of cash"></div>
  <svg class="hero-swoosh" viewBox="0 0 517 222" aria-hidden="true">
    <path d="M300 0 C 320 60, 400 100, 517 108 L517 0 Z" fill="var(--yellow)"/>
    <path d="M300 0 C 320 60, 400 100, 517 108" fill="none" stroke="var(--blue)" stroke-width="3"/>
  </svg>
  <div class="brand-name">Bright Harbor Holdings, LLC</div>
  <div class="call-band">
    <span class="call-label">MAKE A CALL NOW!</span>
    <span class="call-number">
      <svg width="20" height="20" viewBox="0 0 24 24" aria-hidden="true"><circle cx="12" cy="12" r="10.5" fill="none" stroke="currentColor" stroke-width="2"/><path d="M8.5 6.5l2 2-1.2 1.4a7 7 0 0 0 4.8 4.8l1.4-1.2 2 2-1.6 1.8c-4.5-.5-8.7-4.7-9.2-9.2z" fill="currentColor"/></svg>
      0100 555 0199
    </span>
  </div>
</section>

<section class="card card-back">
  <div class="back-heading">Facing foreclosure?<br>Behind on mortgage payments?</div>
  <div class="back-copy">
    <p>If you're in foreclosure or mortgage default, banks can repossess your home and evict you without compensation.</p>
    <p class="alert">Don't let that happen.</p>
    <p>We buy foreclosure homes fast for cash, in any condition, in Seguin, San Antonio, Round Rock, Austin and Huston.</p>
    <p>With cash in your pocket, pay back the bank and walk away<br>with thousands of dollars.</p>
  </div>
  <div class="back-promise">We can find a<br>solutiontogether</div>
  <div class="back-call">
    Call us now at
    <svg width="15" height="15" viewBox="0 0 24 24" aria-hidden="true"><circle cx="12" cy="12" r="10.5" fill="none" stroke="currentColor" stroke-width="2"/><path d="M8.5 6.5l2 2-1.2 1.4a7 7 0 0 0 4.8 4.8l1.4-1.2 2 2-1.6 1.8c-4.5-.5-8.7-4.7-9.2-9.2z" fill="currentColor"/></svg>
    0100 555 0199
  </div>
  <div class="return-brand">Bright Harbor Holdings, LLC</div>
  <div class="return-address">418 Maple Crest Lane,<br>Seguin, TX 78155</div>
  <div class="stamp-box"></div>
</section>

</body>
</html>
```